Redesign for existing homepage

We would like a redesign for our websites 2 column homepage
We provide engine repair and reconditioning services
We would like a cleaner, modern site that works well with our logo colors
Please see the attached brief for more info
Target Market(s)
25 - 45
Industry/Entity Type
Cleaner
Requirements
Must have
- Google Fonts

```html
<!DOCTYPE html>
<html lang="en">
<head>
<meta charset="utf-8">
<title>Harlow Bryce Engine Rebuilders</title>
<link rel="stylesheet" href="https://fonts.googleapis.com/css2?family=Lato:wght@400;700&family=Fredoka:wght@500;600&family=Syncopate:wght@700&family=Tinos&display=swap">
<style>
:root{
  --frame:#3a3a3a;
  --page:#ffffff;
  --blue:#2aa8e0;
  --deep-blue:#1e6fb8;
  --link-blue:#1a7ac4;
  --nav-yellow:#e9e436;
  --nav-line:#c9c42a;
  --panel:#f5f0f0;
  --ink:#111111;
  --rule:#111111;
  --footer:#333333;
  --footer-bar:#8a8a8a;
}
*{box-sizing:border-box;margin:0;padding:0}
html,body{width:960px;height:1200px;overflow:hidden}
body{background:var(--frame);position:relative;font-family:'Lato',sans-serif;color:var(--ink)}
.page{position:absolute;left:38px;top:0;width:882px;height:1200px;background:var(--page)}
.abs{position:absolute}
.brand{left:48px;top:14px;width:346px;height:130px;display:flex;align-items:center;gap:12px}
.brand-dot{width:22px;height:22px;border-radius:50%;background:var(--deep-blue);flex:none}
.brand-name{font-family:'Lato',sans-serif;font-weight:700;font-size:27px;line-height:1.15;color:var(--deep-blue)}
.tagline{left:422px;top:50px;font-family:'Tinos',serif;font-size:27px;line-height:33px;color:var(--blue)}
.social{top:53px;width:30px;height:30px;border-radius:50%;background:var(--blue)}
.appt{right:52px;top:89px;font-family:'Tinos',serif;font-size:16px;color:var(--blue);white-space:nowrap;text-align:right}
.phone{right:52px;top:106px;font-family:'Tinos',serif;font-size:29px;line-height:34px;color:var(--ink);white-space:nowrap;text-align:right}
.nav{left:36px;top:158px;width:884px;height:37px;background:var(--nav-yellow);display:flex;box-shadow:0 3px 4px rgba(0,0,0,.25);overflow:hidden}
.nav a{flex:none;font-family:'Tinos',serif;font-size:15.5px;color:var(--ink);text-decoration:none;padding-left:9px;line-height:37px;white-space:nowrap;border-right:1px solid var(--nav-line)}
.nav a:last-child{border-right:none}
.card{background:var(--page);border-radius:12px;box-shadow:0 5px 6px rgba(0,0,0,.35)}
.card.panel{background:var(--panel)}
.photo{border-radius:2px}
.vrule{background:var(--rule);width:5px}
.hrule{background:var(--rule);height:5px}
.hero-title{font-family:'Fredoka',sans-serif;font-weight:600;font-size:26px;line-height:30px;color:var(--deep-blue)}
.hero-sub{font-size:17.5px}
.body{font-size:14.5px;line-height:18px;white-space:nowrap}
.btn{background:var(--deep-blue);color:var(--nav-yellow);font-family:'Fredoka',sans-serif;font-weight:600;font-size:15px;border-radius:14px;text-align:center;box-shadow:0 0 0 1px #8fc3ea inset}
.welcome{font-family:'Syncopate',sans-serif;font-weight:700;font-size:27px;letter-spacing:1px}
.sub{font-family:'Fredoka',sans-serif;font-weight:500;font-size:14.5px;line-height:18px;color:var(--blue)}
.svc-title{font-family:'Fredoka',sans-serif;font-weight:600;font-size:14.5px;line-height:17px;color:var(--link-blue)}
.more{background:var(--link-blue);color:var(--nav-yellow);font-family:'Fredoka',sans-serif;font-weight:600;font-size:14px;border-radius:12px;width:72px;height:22px;line-height:22px;text-align:center}
.footer{top:1092px;height:65px;background:var(--footer)}
.footer-bar{top:1159px;height:41px;background:var(--footer-bar);text-align:center;font-family:'Tinos',serif;font-size:13px;letter-spacing:.8px;line-height:18px;padding-top:3px}
</style>
</head>
<body>
<div class="page">
  <div class="abs brand" style="left:10px"><span class="brand-dot"></span><span class="brand-name">Harlow Bryce<br>Engine Rebuilders</span></div>
  <div class="abs tagline" style="left:384px">Engine Repairs &amp;<br>Reconditioning Specialist</div>
  <div class="abs social" style="left:798px"></div>
  <div class="abs social" style="left:836px"></div>
</div>
<div class="abs appt">For Appointment</div>
<div class="abs phone">04.555.0148</div>

<nav class="abs nav">
  <a style="width:67px">HOME</a><a style="width:99px">ABOUT US</a><a style="width:180px">TRADE CUSTOMERS</a><a style="width:149px">MAKE AN ENTRY</a><a style="width:267px">RACE &amp; CLASSIC CARS ENGINES</a><a style="width:122px">CONTACT US</a>
</nav>

<div class="abs card" style="left:53px;top:206px;width:510px;height:351px"></div>
<div class="abs photo" role="img" aria-label="Mechanic in red overalls standing in a workshop with cars on lifts" style="left:70px;top:221px;width:480px;height:320px;background:linear-gradient(180deg,#b9bcc0 0%,#8e9196 45%,#a86a55 75%,#9a4c3c 100%)"></div>
<div class="abs vrule" style="left:570px;top:219px;height:362px"></div>

<div class="abs card panel" style="left:581px;top:206px;width:323px;height:351px"></div>
<div class="abs hero-title" style="left:602px;top:225px">Specialist engine repair<br>and reconditioning</div>
<div class="abs hero-sub" style="left:603px;top:287px">To have your car running as its best</div>
<div class="abs body" style="left:604px;top:324px">
  <p style="margin-bottom:8px">Do you have a personal or family car<br>that needs a repair?</p>
  <p style="margin-bottom:10px">Have a classic car that needs specialist<br>engine work?</p>
  <p style="margin-bottom:10px">Own a race car that needs specialist<br>engine repairs?</p>
  <p>Are you a garage owner, needing to outsource<br>an engine machining job from one of your<br>customers?</p>
</div>
<div class="abs btn" style="left:727px;top:518px;width:161px;height:32px;line-height:32px">Make an Enquiry Now</div>

<div class="abs hrule" style="left:57px;top:585px;width:507px"></div>
<div class="abs vrule" style="left:570px;top:585px;height:493px"></div>
<div class="abs hrule" style="left:581px;top:585px;width:323px"></div>

<div class="abs card" style="left:53px;top:590px;width:510px;height:490px"></div>
<div class="abs welcome" style="left:84px;top:596px">WELCOME</div>
<div class="abs sub" style="left:84px;top:640px">Professional and knowledgeable<br>workshop staff</div>
<div class="abs body" style="left:84px;top:692px">We have an experienced and friendly team that are capable<br>of providing you with a fantastic service.</div>
<div class="abs body" style="left:84px;top:744px">The staff are passionate about cars and dedicated to giving<br>your vehicle the highest standard of service.</div>
<div class="abs sub" style="left:84px;top:795px">Qualified &amp; experienced engine machinists</div>
<div class="abs body" style="left:84px;top:830px">The machinists in my workshop are qualified and experienced<br>in their field of work. With all the advancements in modern engine<br>technology, it takes a specialist team to stay up to date.</div>
<div class="abs sub" style="left:84px;top:899px">Attention to the finer details</div>
<div class="abs body" style="left:84px;top:934px">The team here at HBER will take the time<br>to ensure that they have completed any<br>&nbsp;job to specification.</div>
<div class="abs body" style="left:84px;top:1004px">You can be sure any work done on your<br>classic car or race car will be to the highest<br>standard.</div>
<div class="abs" role="img" aria-label="Workshop building front with cars parked outside" style="left:355px;top:938px;width:197px;height:118px;background:linear-gradient(180deg,#ffffff 0%,#8a4e3c 20%,#a8664f 45%,#e8e6e2 60%,#c9c9c9 100%)"></div>

<div class="abs card panel" style="left:581px;top:590px;width:323px;height:490px"></div>

<div class="abs svc-title" style="left:587px;top:603px">Private Vehicle Service</div>
<div class="abs body" style="left:588px;top:628px">Get an efficient and<br>honest diagnosis, along<br>with repair work that<br>will have your car running<br>smoothly...</div>
<div class="abs more" style="left:629px;top:719px">More...</div>
<div class="abs" role="img" aria-label="Hands cupped around a globe against a cloudy sky" style="left:756px;top:602px;width:138px;height:138px;background:linear-gradient(160deg,#7fa9d6,#dfe9f3 50%,#4f7fb5)"></div>

<div class="abs svc-title" style="left:590px;top:760px">Needs service and<br>repari?</div>
<div class="abs body" style="left:590px;top:796px">Get an efficient and<br>honest diagnosis, along<br>with repair work that<br>will have your car running<br>smoothly...</div>
<div class="abs more" style="left:629px;top:886px">More...</div>
<div class="abs" role="img" aria-label="Car raised on a lift inside a repair garage" style="left:757px;top:762px;width:138px;height:137px;background:linear-gradient(160deg,#d9dde2,#8c9299 55%,#b1aba5)"></div>

<div class="abs svc-title" style="left:589px;top:925px">Interesting in becoming<br>a trade customer?</div>
<div class="abs body" style="left:589px;top:963px">You can outsource your<br>the specialist machining<br>jobs to us at very<br>competitive rates.</div>
<div class="abs more" style="left:629px;top:1038px">More...</div>
<div class="abs" role="img" aria-label="Busy garage floor with several cars on lifts" style="left:758px;top:925px;width:137px;height:135px;background:linear-gradient(160deg,#e9ecef,#a9adb2 50%,#cfd2d5)"></div>

<div class="abs footer" style="left:40px;width:880px"></div>
<div class="abs footer-bar" style="left:40px;width:880px">Privacy Policy - Terms - News - Sitemap<br>2014 Company Name. All right reserved. Terms of Use</div>
</body>
</html>
```